Book cover for a New Adult, romance/ contemporary novel.

I need a full front, back, and spine cover for my upcoming book. The novel is a romance/ coming of age book and is similar to Every Quiet Harbor by Marisol Pekkar. My main audience is women in their late teens/ early 20's. The book is an emotional, reminiscent piece and I would love to see some cover designs with a darker palette like Waiting on Tuesday, Nine Rooms Away, or Lucian and Omar (but I also adore some lighter covers, especially those that feature the couple such as Any Given Then or Until Each Dawn). Feel free to send some minimal designs as well if you have any! A great idea of that would be the cover for Salt and Clover or Waiting on Tuesday. If you go with a minimal design, I'd love to see silhouettes or maybe a burning candle. Another possible idea I thought of would be a scene at a concert with the crowd silhouetted and then my main character (more details on her below) standing in the middle of it all. I prefer animation/drawing etc over real models. But feel free to send me whatever you think might match the vibe, I'd love to see anything you have in mind! Some main symbols in my book are stars and candles. The main character (Hana) is a female Korean with brown, medium length straight hair, and the love interest (Theo) is a tall and thin male Caucasian with curly brown hair. The book is openly emotional, wistful, and sets an ache in your chest, so I can't wait to see what designs you artists come up with! (My barcode will need to be included on the back cover, and I am getting that soon!)
The title is "A Map Toward Dusk" and the author's name is Brynn Okafor. The book's dimensions will be 5.5x8.25. The blurb for the back cover is:
When happily ever falls apart, all you can do is move forward… and reminisce. Hana Yoon returns home from college following a tragic incident she can’t bring herself to talk about and a breakup with her boyfriend, Theo Marchetti. Finding it difficult to confront her traumas, she begins therapy. Hana takes the therapist on a rollercoaster journey of her college life, retelling the events that caused her relationship to spiral out of control and led to her dropping out of pre-med despite that being her life-long dream. Hana sets out to remember how things were before everything got so messed up, and figure out how to continue living now that they are.
The author bio for the back cover is:
Brynn Okafor is the author of A Restless Hour. She is a self published writer from Las Vegas who likes to pretend she’s currently in a New York bookstore, drinking a latte, while listening to a carefully curated playlist. When she’s not writing, Brynn is taking care of her plant babies and cuddling with the cutest puppy in the world.

```html
<!DOCTYPE html>
<html lang="en">
<head>
<meta charset="utf-8">
<title>A Map Toward Dusk – Full Cover Wraps</title>
<link rel="stylesheet" href="https://fonts.googleapis.com/css2?family=Lato:ital,wght@0,300;0,400;0,700;1,700&family=Mrs+Saint+Delafield&display=swap">
<style>
  :root {
    --page-bg: #f4f4f4;
    --cover-bg: #000000;
    --ink: #ffffff;
    --barcode-bg: #ffffff;
    --gold: #e0a93e;
    --gold-deep: #7a5414;
    --blue: #2f5cf0;
    --blue-deep: #10297a;
    --font-sans: "Lato", Arial, sans-serif;
    --font-script: "Mrs Saint Delafield", cursive;
  }
  * { box-sizing: border-box; margin: 0; padding: 0; }
  html, body {
    width: 1200px; height: 873px; overflow: hidden;
    background: var(--page-bg);
  }
  .sheet { position: relative; width: 1200px; height: 873px; }

  .wrap {
    position: absolute; left: 301px; width: 598px; height: 423px;
    background: var(--cover-bg); color: var(--ink); overflow: hidden;
    font-family: var(--font-sans);
  }
  .wrap--gold { top: 0; --accent: var(--gold); --accent-deep: var(--gold-deep); }
  .wrap--blue { top: 449px; --accent: var(--blue); --accent-deep: var(--blue-deep); }

  /* silhouette artwork area: head + neck in soft gradients */
  .art { position: absolute; }
  .art__head, .art__neck { position: absolute; }
  .art__head {
    left: 0; top: 0; width: 100%; height: 62%;
    border-radius: 50% 48% 44% 52%;
    background:
      radial-gradient(ellipse 60% 40% at 62% 14%, var(--accent) 0%, rgba(0,0,0,0) 70%),
      radial-gradient(ellipse 30% 45% at 84% 42%, var(--accent) 0%, rgba(0,0,0,0) 75%),
      radial-gradient(ellipse at 50% 45%, var(--accent-deep) 0%, rgba(0,0,0,.0) 72%);
  }
  .art__neck {
    left: 18%; top: 52%; width: 62%; height: 48%;
    border-radius: 40% 50% 30% 30%;
    transform: skewX(-14deg);
    background:
      radial-gradient(ellipse 35% 45% at 55% 35%, var(--accent) 0%, rgba(0,0,0,0) 75%),
      radial-gradient(ellipse at 45% 60%, var(--accent-deep) 0%, rgba(0,0,0,0) 72%);
  }

  /* back cover */
  .back { position: absolute; left: 0; top: 0; width: 270px; height: 423px; }
  .back__art { left: 64px; top: 48px; width: 180px; height: 372px; opacity: .32; }
  .author {
    position: absolute; left: 0; width: 100%; text-align: center;
    font-weight: 300; font-size: 21px; line-height: 1; letter-spacing: .3px; top: 18px;
  }
  .back__title {
    position: absolute; left: 26px; top: 48px; width: 236px;
    font-family: var(--font-script); font-size: 35px; line-height: 1; white-space: nowrap;
  }
  .blurb {
    position: absolute; left: 28px; top: 94px; width: 229px;
    font-size: 10.5px; line-height: 12.9px; text-align: justify; font-weight: 400;
  }
  .blurb::first-letter { font-size: 18px; line-height: 1; }
  .bio {
    position: absolute; left: 28px; top: 298px; width: 242px;
    font-size: 9.9px; line-height: 12px; text-align: justify;
  }
  .bio__text { display: block; }
  .bio strong { font-weight: 700; font-size: 10.5px; }
  .bio em { font-weight: 700; font-style: italic; }
  .bio__spacer { float: right; width: 0; height: 49px; }
  .barcode-box {
    float: right; clear: right; width: 98px; height: 58px;
    margin-left: 8px; background: var(--barcode-bg);
  }

  /* spine */
  .spine { position: absolute; left: 270px; top: 0; width: 46px; height: 423px; }
  .spine__text {
    position: absolute; left: 50%; top: 28px;
    writing-mode: vertical-rl; transform: translateX(-50%);
    display: flex; align-items: center; gap: 34px; white-space: nowrap;
  }
  .spine__author { font-weight: 300; font-size: 15px; letter-spacing: .3px; }
  .spine__title { font-family: var(--font-script); font-size: 22px; }

  /* front cover */
  .front { position: absolute; left: 316px; top: 0; width: 282px; height: 423px; }
  .front__art { left: 22px; top: 48px; width: 214px; height: 372px; opacity: .75; }
  .front .author { text-align: left; left: 0; padding-left: 0; width: 100%; text-align: center; }
  .front__title {
    position: absolute; left: 0; top: 0; width: 100%; height: 100%;
    font-family: var(--font-script); font-weight: 400; font-size: 70px; line-height: 1;
  }
  .front__title span { position: absolute; white-space: nowrap; }
  .front__title .l1 { left: 62px; top: 80px; }
  .front__title .l2 { left: 84px; top: 180px; }
  .front__title .l3 { left: 92px; top: 300px; }
</style>
</head>
<body>
<main class="sheet">

  <section class="wrap wrap--gold" aria-label="Full cover wrap, gold colourway">
    <div class="back">
      <div class="art back__art" role="img" aria-label="Faint gold silhouette of a woman's head in profile filled with orange stars and constellation lines"><span class="art__head"></span><span class="art__neck"></span></div>
      <p class="author">BRYNN OKAFOR</p>
      <p class="back__title">A Map Toward Dusk</p>
      <p class="blurb">When happily ever falls apart, all you can do is move forward… and reminisce. Hana Yoon returns home from college following a tragic incident she can’t bring herself to talk about and a breakup with her boyfriend, Theo Marchetti. Finding it difficult to confront her traumas, she begins therapy. Hana takes the therapist on a rollercoaster journey of her college life, retelling the events that caused her relationship to spiral out of control and led to her dropping out of pre-med despite that being her life-long dream. Hana sets out to remember how things were before everything got so messed up, and figure out how to continue living now that they are.</p>
      <div class="bio"><span class="bio__spacer"></span><span class="barcode-box" aria-label="Barcode area"></span><span class="bio__text"><strong>Brynn Okafor</strong> is the author of <em>A Restless Hour</em>. She is a self published writer from Las Vegas who likes to pretend she’s currently in a New York bookstore, drinking a latte, while listening to a carefully curated playlist. When she’s not writing, Brynn is taking care of her plant babies and cuddling with the cutest puppy in the world.</span></div>
    </div>
    <div class="spine">
      <div class="spine__text"><span class="spine__author">BRYNN OKAFOR</span><span class="spine__title">A Map Toward Dusk</span></div>
    </div>
    <div class="front">
      <div class="art front__art" role="img" aria-label="Gold silhouette of a woman's head in profile filled with orange stars and constellation lines"><span class="art__head"></span><span class="art__neck"></span></div>
      <p class="author">BRYNN OKAFOR</p>
      <h1 class="front__title"><span class="l1">A Map</span><span class="l2">Toward</span><span class="l3">Dusk</span></h1>
    </div>
  </section>

  <section class="wrap wrap--blue" aria-label="Full cover wrap, blue colourway">
    <div class="back">
      <div class="art back__art" role="img" aria-label="Faint blue silhouette of a woman's head in profile filled with blue stars and constellation lines"><span class="art__head"></span><span class="art__neck"></span></div>
      <p class="author">BRYNN OKAFOR</p>
      <p class="back__title">A Map Toward Dusk</p>
      <p class="blurb">When happily ever falls apart, all you can do is move forward… and reminisce. Hana Yoon returns home from college following a tragic incident she can’t bring herself to talk about and a breakup with her boyfriend, Theo Marchetti. Finding it difficult to confront her traumas, she begins therapy. Hana takes the therapist on a rollercoaster journey of her college life, retelling the events that caused her relationship to spiral out of control and led to her dropping out of pre-med despite that being her life-long dream. Hana sets out to remember how things were before everything got so messed up, and figure out how to continue living now that they are.</p>
      <div class="bio"><span class="bio__spacer"></span><span class="barcode-box" aria-label="Barcode area"></span><span class="bio__text"><strong>Brynn Okafor</strong> is the author of <em>A Restless Hour</em>. She is a self published writer from Las Vegas who likes to pretend she’s currently in a New York bookstore, drinking a latte, while listening to a carefully curated playlist. When she’s not writing, Brynn is taking care of her plant babies and cuddling with the cutest puppy in the world.</span></div>
    </div>
    <div class="spine">
      <div class="spine__text"><span class="spine__author">BRYNN OKAFOR</span><span class="spine__title">A Map Toward Dusk</span></div>
    </div>
    <div class="front">
      <div class="art front__art" role="img" aria-label="Blue silhouette of a woman's head in profile filled with blue stars and constellation lines"><span class="art__head"></span><span class="art__neck"></span></div>
      <p class="author">BRYNN OKAFOR</p>
      <h2 class="front__title"><span class="l1">A Map</span><span class="l2">Toward</span><span class="l3">Dusk</span></h2>
    </div>
  </section>

</main>
</body>
</html>
```